Anzeigengestaltung für Gas- und Wasserinstallationsunternehmen
Zielgruppe
Gas- und Wasserinstallation, wir bauen, warten und sanieren Bäder und Heizungsanlagen
Wir wollen Leute im Alter 26-45 Jahre ansprechen, mit Berufserfahrung
Aufgabenstellung
Dass wir einen Kundendienstmonteur für Öl- und Gasfeuerung suchen

```html
<!DOCTYPE html>
<html lang="de">
<head>
<meta charset="utf-8">
<title>Stellenanzeige Kundendienstmonteur</title>
<link href="https://fonts.googleapis.com/css2?family=Jost:wght@400;500;600;700&display=swap" rel="stylesheet">
<style>
  :root {
    --page-bg: #bdbdbd;
    --hero-dark: #2a0f08;
    --hero-mid: #4a1a0c;
    --fire-hot: #f2a23a;
    --fire-deep: #8a2a0e;
    --panel: rgba(4, 26, 18, 0.92);
    --band-green: #16a54c;
    --band-teal: #0f8f86;
    --band-blue: #0a6fc2;
    --white: #ffffff;
  }
  * { box-sizing: border-box; margin: 0; padding: 0; }
  html, body { width: 1200px; height: 808px; overflow: hidden; }
  body { background: var(--page-bg); font-family: "Jost", sans-serif; color: var(--white); position: relative; }

  .ad {
    position: absolute; left: 82px; top: 32px; width: 1040px; height: 733px;
    overflow: hidden; box-shadow: 0 2px 6px rgba(0,0,0,0.35);
  }
  .hero {
    position: absolute; left: 0; top: 0; width: 1040px; height: 518px;
    background: linear-gradient(180deg, var(--hero-dark) 0%, var(--hero-mid) 60%, #1e0c07 100%);
  }
  .hero-photo {
    position: absolute; left: 0; top: 0; width: 480px; height: 518px;
    background:
      radial-gradient(ellipse 55% 60% at 55% 45%, var(--fire-hot) 0%, rgba(242,162,58,0.5) 45%, rgba(138,42,14,0) 80%),
      linear-gradient(90deg, #3a1409 0%, var(--fire-deep) 50%, rgba(74,26,12,0) 100%);
  }

  .headline { position: absolute; font-weight: 700; line-height: 1; letter-spacing: 0.3px; }
  .headline-1 { left: 356px; top: 34px; font-size: 54px; }
  .headline-2 { left: 424px; top: 100px; font-size: 54px; }
  .headline-2 .aside { font-size: 29px; margin-left: 14px; }
  .headline-3 { right: 52px; top: 160px; font-size: 28px; }

  .job-panel {
    position: absolute; left: 445px; top: 215px; width: 595px; height: 287px;
    background: var(--panel); padding: 16px 0 0 29px;
  }
  .job-title { font-size: 22px; font-weight: 600; line-height: 1.28; }
  .requirements { list-style: none; margin-top: 14px; font-size: 16px; line-height: 23.5px; }
  .requirements li { position: relative; padding-left: 17px; }
  .requirements li::before {
    content: ""; position: absolute; left: 1px; top: 9px;
    width: 5px; height: 5px; border-radius: 50%; background: var(--white);
  }

  .band {
    position: absolute; left: 0; top: 518px; width: 1040px; height: 215px;
    background: linear-gradient(90deg, var(--band-green) 0%, var(--band-teal) 55%, var(--band-blue) 100%);
  }
  .brand { position: absolute; left: 32px; top: 30px; display: flex; align-items: center; gap: 22px; }
  .brand-dot { width: 64px; height: 64px; border-radius: 50%; background: var(--white); }
  .brand-name { font-size: 34px; font-weight: 600; letter-spacing: 0.5px; }

  .apply-note { position: absolute; left: 518px; top: 32px; font-size: 17px; line-height: 21px; }

  .company { position: absolute; left: 39px; top: 125px; font-size: 17px; line-height: 22px; font-style: normal; }
  .company strong { font-weight: 600; }
  .phone { position: absolute; left: 462px; top: 148px; font-size: 17px; line-height: 22px; }
  .web { position: absolute; right: 42px; top: 148px; font-size: 17px; line-height: 22px; text-align: right; }
</style>
</head>
<body>
  <main class="ad">
    <section class="hero">
      <div class="hero-photo" role="img" aria-label="Foto eines Handwerkers mit Hammer und Bohrmaschine vor lodernden Flammen"></div>

      <h1 class="headline headline-1">Feuer und Flamme</h1>
      <p class="headline headline-2">für Ihren Beruf?<span class="aside">Wir auch!</span></p>
      <p class="headline headline-3">Kommen Sie in unser Team.</p>

      <div class="job-panel">
        <h2 class="job-title">Wir suchen einen Kundendienstmonteur<br>für Öl- und Gasfeuerung (m/w):</h2>
        <ul class="requirements">
          <li>abgeschlossene Ausbildung als Gas-Wasser- oder<br>Anlagenmechaniker/in Sanitär /Heizung</li>
          <li>Berufserfahrung im vorgenannten Ausbildungsfeld</li>
          <li>lösungsorientierte, selbstständige und teamorientierte Arbeitsweise</li>
          <li>Führerschein Klasse B</li>
          <li>aufgeschlossen gegenüber neuen Herausforderungen<br>mit Leidenschaft für den Beruf und dem Service beim Kunden</li>
          <li>Zukunftsorientiertes Denken und Arbeiten</li>
        </ul>
      </div>
    </section>

    <footer class="band">
      <div class="brand">
        <span class="brand-dot"></span>
        <span class="brand-name">FELDKAMP WÄRME</span>
      </div>

      <p class="apply-note">Wir freuen uns auf Ihre aussagekräftigen Unterlagen<br>(Anschreiben, Lebenslauf mit Lichtbild, Zeugnissen) per Post<br>oder kommen Sie nach telefonischer Absprache einfach<br>persönlich vorbei und überzeugen uns!</p>

      <address class="company">
        <strong>Feldkamp Wärme GmbH</strong><br>
        Gesellschaft für Versorgungsanlagen mbH<br>
        Lindenweg 14 | 10115 Berlin
      </address>
      <p class="phone">Tel. : +49 (0)30 55 01 - 4200<br>Fax : +49 (0)30 55 01 - 4201</p>
      <p class="web">info@feldkamp-waerme.de<br>www.feldkamp-waerme.de</p>
    </footer>
  </main>
</body>
</html>
```